Real Estate Company Needs Business Card Designed

We need a business card design for a new real estate company based in Campbell, CA (Silicon Valley). We plan to improve the residential real estate industry by using technology to improve customer experience. We would like to see designs that use a black background. The final design should communicate sophistication and customer service, as well as stability and technology.

Industry/Entity Type

Real Estate

Requirements
Must have
• Black background

```html
<!DOCTYPE html>
<html lang="en">
<head>
<meta charset="utf-8">
<title>Solvara Business Card</title>
<link href="https://fonts.googleapis.com/css2?family=Source+Sans+3:wght@400;500&display=swap" rel="stylesheet">
<style>
  :root {
    --paper: #eeeeef;
    --card: #0b0b0c;
    --blue: #3f7bc3;
    --red: #d42a3c;
    --card-w: 500px;
    --card-h: 290px;
  }
  * { box-sizing: border-box; margin: 0; padding: 0; }
  html, body { width: 1200px; height: 900px; overflow: hidden; }
  body {
    background: var(--paper);
    font-family: "Source Sans 3", "Segoe UI", sans-serif;
    position: relative;
  }
  .card {
    position: absolute;
    width: var(--card-w);
    height: var(--card-h);
    background: var(--card);
    border-radius: 28px;
    overflow: hidden;
    box-shadow: 0 10px 24px rgba(0,0,0,0.18);
  }
  .card--back { left: 70px; top: 305px; }
  .card--front { left: 630px; top: 305px; }

  /* back side */
  .back-brand {
    position: absolute;
    left: 0; right: 0; top: 112px;
    text-align: center;
  }
  .back-brand__name {
    color: var(--blue);
    font-size: 66px;
    font-weight: 500;
    letter-spacing: 1px;
    line-height: 1;
  }
  .back-brand__web {
    margin-top: 10px;
    color: var(--red);
    font-size: 17px;
    letter-spacing: 6px;
  }

  /* front side */
  .front-brand {
    position: absolute;
    left: 44px; top: 56px;
    color: var(--blue);
    font-size: 38px;
    font-weight: 500;
    letter-spacing: 1px;
    line-height: 1;
  }
  .person {
    position: absolute;
    left: 290px; top: 122px;
    font-size: 17px;
    white-space: nowrap;
  }
  .person__name { color: var(--red); }
  .person__role { color: var(--blue); font-size: 14px; }
  .contact, .address {
    position: absolute;
    list-style: none;
    font-size: 14px;
    line-height: 20px;
    color: var(--blue);
  }
  .contact { left: 44px; top: 168px; }
  .contact__label { color: var(--red); }
  .address { left: 290px; top: 188px; }
  .front-rule {
    position: absolute;
    left: 0; right: 0; bottom: 17px;
    height: 1px;
    background: var(--red);
  }
  .front-band {
    position: absolute;
    left: 0; right: 0; bottom: 0;
    height: 14px;
    background: var(--blue);
  }
</style>
</head>
<body>
  <section class="card card--back" aria-label="Card back">
    <div class="back-brand">
      <div class="back-brand__name">SOLVARA</div>
      <div class="back-brand__web">www.solvara.com</div>
    </div>
  </section>

  <section class="card card--front" aria-label="Card front">
    <div class="front-brand">SOLVARA</div>
    <p class="person"><span class="person__name">Daniel Mercer,</span> <span class="person__role">Director</span></p>
    <ul class="contact">
      <li><span class="contact__label">p:</span> 1234 555 987</li>
      <li><span class="contact__label">e:</span> mercer@solvara.com.au</li>
      <li>www.solvara.com.au</li>
    </ul>
    <ul class="address">
      <li>SOLVARA HOLDINGS Pty Ltd</li>
      <li>PO Box 000, Harbour Point,</li>
      <li>NSW 0000 Australia</li>
    </ul>
    <div class="front-rule"></div>
    <div class="front-band"></div>
  </section>
</body>
</html>
```